Maple Hollow Campground Billboard

We need an eye-catching, traffic-stopping design for a 15 ft x 10 ft billboard that will be located near the turn-off to our RV park in Colorado. Our park is located on the banks of the Rio Grande River and we want to emphasize that we have shady spots on the river. This is a link to our website www.maplehollowcampground.com and it will give you an idea about our park and what we have to offer. The billboard will be double-sided and face both directions of a busy highway. The park and the river is not visible from the highway, so we want to attract attention.

Target Market(s)

RV travelers on US Hwy 160 in South Fork, Colorado

Font styles to use
Sans Serif

Colors

Designer to choose colors to be used in the design.

Requirements
Must have
• Simple, eye-catching message.
Nice to have
• Incorporate our logo and give directions.
Should not have
• Too much information that can't be read while speeding down a busy highway.

```html
<!DOCTYPE html>
<html lang="en">
<head>
<meta charset="utf-8">
<title>Maple Hollow Campground Billboard</title>
<link rel="stylesheet" href="https://fonts.googleapis.com/css2?family=Francois+One&family=Oswald:wght@400;500&display=swap">
<style>
  :root {
    --frame-grey: #a9a9a9;
    --paper: #ffffff;
    --forest: #003b16;
    --leaf: #1aa54a;
    --navy: #2e3192;
    --lens-ring: #2b2962;
    --lens-rim: #3a397a;
  }
  * { margin: 0; padding: 0; box-sizing: border-box; }
  html, body { width: 1200px; height: 821px; overflow: hidden; background: var(--frame-grey); }
  .billboard { position: relative; width: 1200px; height: 821px; background: var(--frame-grey); }
  .panel { position: absolute; left: 48px; top: 37px; width: 1113px; height: 742px; background: var(--paper); overflow: hidden; }

  .brand {
    position: absolute; left: 40px; top: 60px; width: 250px; height: 120px;
    display: flex; align-items: center; gap: 12px;
    font-family: "Francois One", sans-serif; font-size: 30px; line-height: 1.05;
    color: var(--forest); text-transform: uppercase;
  }
  .brand-dot { flex: none; width: 26px; height: 26px; border-radius: 50%; background: var(--leaf); }

  .photo-campsite {
    position: absolute; left: 302px; top: 0; width: 461px; height: 232px;
    background: linear-gradient(180deg, #8fae6a 0%, #4f6b34 45%, #c9c7b8 70%, #6f7a4a 100%);
  }
  .photo-office {
    position: absolute; left: 763px; top: 0; width: 350px; height: 232px;
    background: linear-gradient(180deg, #5f8a3c 0%, #7a5a3e 45%, #8b6547 75%, #5c4a36 100%);
  }

  .band { position: absolute; left: 0; background: var(--forest); color: var(--paper); font-family: "Francois One", sans-serif; text-align: center; }
  .band-top { top: 232px; width: 1113px; height: 61px; }
  .band-top .band-text { position: absolute; left: 0; width: 600px; top: 2px; font-size: 47px; line-height: 57px; letter-spacing: 1px; }
  .band-call { top: 509px; width: 690px; height: 137px; }
  .band-call .band-text { width: 600px; }
  .call-label { display: block; font-size: 50px; line-height: 56px; margin-top: 10px; }
  .call-number { display: block; font-size: 64px; line-height: 64px; }

  .headline { position: absolute; left: 0; width: 600px; top: 302px; text-align: center; font-family: "Francois One", sans-serif; font-size: 72px; line-height: 82px; color: var(--leaf); letter-spacing: 1px; }
  .subline { position: absolute; left: 0; width: 600px; top: 388px; text-align: center; font-family: "Oswald", sans-serif; font-weight: 400; font-size: 54px; line-height: 60px; color: var(--navy); }

  .email { position: absolute; left: 0; width: 600px; top: 653px; text-align: center; font-family: "Francois One", sans-serif; font-size: 24px; color: var(--leaf); }

  .lens { position: absolute; left: 0; top: 0; width: 1113px; height: 742px; }
</style>
</head>
<body>
<div class="billboard">
  <div class="panel">
    <div class="brand"><span class="brand-dot"></span><span>Maple Hollow Campground</span></div>

    <div class="photo-campsite" role="img" aria-label="Shaded campsite with a pop-up camper and screen tent under tall trees"></div>
    <div class="photo-office" role="img" aria-label="A-frame wooden campground office among green trees"></div>

    <div class="band band-top"><div class="band-text">RV CAMPING SITES</div></div>

    <div class="headline">SHADE SPOTS</div>
    <div class="subline">CLOSE TO THE<br>RIO GRANDE RIVER</div>

    <div class="band band-call">
      <div class="band-text">
        <span class="call-label">CALL US</span>
        <span class="call-number">719.555.0142</span>
      </div>
    </div>

    <div class="email">manager@maplehollowcampground.com</div>

    <svg class="lens" viewBox="0 0 1113 742" aria-hidden="false">
      <defs>
        <linearGradient id="riverScene" x1="0" y1="0" x2="0" y2="1">
          <stop offset="0" stop-color="#c9d3dc"/>
          <stop offset="0.3" stop-color="#7fa04e"/>
          <stop offset="0.6" stop-color="#5d7f35"/>
          <stop offset="0.8" stop-color="#8fa45a"/>
          <stop offset="1" stop-color="#b9ae95"/>
        </linearGradient>
      </defs>
      <line x1="990" y1="610" x2="1135" y2="760" stroke="var(--lens-ring)" stroke-width="66" stroke-linecap="round"/>
      <circle cx="810" cy="429" r="227" fill="none" stroke="var(--lens-ring)" stroke-width="46"/>
      <path d="M 810 202 A 227 227 0 0 1 1037 429" fill="none" stroke="var(--lens-rim)" stroke-width="46"/>
      <circle cx="810" cy="429" r="204" fill="url(#riverScene)" role="img" aria-label="Riverbank with trees and parked RVs beside the Rio Grande"/>
    </svg>
  </div>
</div>
</body>
</html>
```